Harlow Auto , a Dealership and Repair Shop in Marengo Iowa

Harlow Auto is a repair shop and auto sales dealership that offers oil changes, alignments, tires, air conditioning work, computer diagnostics. Focused on Vantras, Marlo and Brisk. Small business with less than 10 employees. Billboard sign is in town and not the larger billboard
billboard is 8ft x 18ft

Target Market(s)

General public

Industry/Entity Type

automotive

Font styles to use
Serif
Sans Serif

Colors

Designer to choose colors to be used in the design.

Requirements
Must have
• Located 2 miles north of Marengo. Sales and service. Phone number 319-555-0187
Nice to have
• Picture of a car or truck, or both. picture of wrench
Should not have
• Not sure

```html
<!DOCTYPE html>
<html lang="en">
<head>
<meta charset="utf-8">
<title>Harlow Auto Billboard</title>
<link href="https://fonts.googleapis.com/css2?family=Poppins:wght@600;700;800&display=swap" rel="stylesheet">
<style>
  :root {
    --royal: #2f4db3;
    --royal-deep: #24409f;
    --royal-band: #3654c2;
    --white: #ffffff;
    --stage: #e9ecf1;
  }
  * { margin: 0; padding: 0; box-sizing: border-box; }
  html, body { width: 1200px; height: 821px; overflow: hidden; background: var(--stage); }
  .canvas { position: relative; width: 1200px; height: 821px; }
  .billboard {
    position: absolute; left: 40px; top: 161px;
    width: 1120px; height: 498px; overflow: hidden;
    background: var(--royal);
    font-family: "Poppins", sans-serif;
  }
  .billboard-shapes { position: absolute; inset: 0; width: 100%; height: 100%; }
  .headline {
    position: absolute; left: 58px; top: 92px;
    color: var(--white); font-weight: 800; font-size: 66px;
    line-height: 1.08; letter-spacing: -0.5px; text-transform: uppercase;
  }
  .location {
    position: absolute; left: 58px; top: 272px;
    color: var(--white); font-weight: 600; font-size: 25px;
    line-height: 1.22; text-transform: uppercase;
  }
  .phone-pill {
    position: absolute; left: 40px; top: 402px;
    width: 400px; height: 66px; border-radius: 12px;
    background: var(--white);
    display: flex; align-items: center;
  }
  .phone-icon {
    position: absolute; left: -6px; top: -7px;
    width: 80px; height: 80px; border-radius: 50%;
    background: var(--white); border: 6px solid var(--royal);
    display: flex; align-items: center; justify-content: center;
  }
  .phone-number {
    margin-left: 92px; color: var(--royal);
    font-weight: 800; font-size: 42px; letter-spacing: -0.5px;
  }
  .brand {
    position: absolute; right: 40px; top: 30px; text-align: center;
    color: var(--royal);
  }
  .brand-name { font-weight: 800; font-size: 40px; line-height: 1; }
  .brand-town { font-weight: 700; font-size: 14px; margin-top: 4px; }
</style>
</head>
<body>
<div class="canvas">
  <section class="billboard">
    <svg class="billboard-shapes" viewBox="0 0 1120 498" preserveAspectRatio="none">
      <defs>
        <linearGradient id="sceneFill" x1="0" y1="0" x2="0" y2="1">
          <stop offset="0" stop-color="#e6e2dc"/>
          <stop offset="0.4" stop-color="#b9b4ad"/>
          <stop offset="0.65" stop-color="#7c8672"/>
          <stop offset="1" stop-color="#8e949c"/>
        </linearGradient>
        <linearGradient id="truckFill" x1="0" y1="0" x2="1" y2="1">
          <stop offset="0" stop-color="#3558bd"/>
          <stop offset="1" stop-color="#1b2c63"/>
        </linearGradient>
        <linearGradient id="panelFill" x1="0" y1="0" x2="1" y2="1">
          <stop offset="0" stop-color="#3251b8"/>
          <stop offset="1" stop-color="#2a46a8"/>
        </linearGradient>
        <clipPath id="photoClip">
          <path d="M722 0 H1120 V498 H800 C660 380 650 150 722 0 Z"/>
        </clipPath>
      </defs>
      <rect class="panel-blue" width="1120" height="498" fill="url(#panelFill)"/>
      <path class="curve-white-outer" d="M660 0 H1120 V498 H610 C520 380 540 160 660 0 Z" fill="#ffffff"/>
      <path class="curve-blue-band" d="M690 0 H1120 V498 H740 C600 380 605 150 690 0 Z" fill="#3654c2"/>
      <path class="curve-white-inner" d="M722 0 H1120 V498 H800 C660 380 650 150 722 0 Z" fill="#ffffff"/>
      <g clip-path="url(#photoClip)">
        <rect class="scene-photo" role="img" aria-label="Photo of a mountain road at sunset"
              x="640" y="108" width="480" height="390" fill="url(#sceneFill)"/>
        <rect class="truck-photo" role="img" aria-label="Photo of a blue pickup truck"
              x="700" y="150" width="380" height="310" rx="34" fill="url(#truckFill)"/>
      </g>
    </svg>

    <h1 class="headline">Sales and<br>Service</h1>
    <p class="location">Located<br>2 miles north<br>of Marengo</p>

    <div class="phone-pill">
      <span class="phone-icon">
        <svg width="40" height="40" viewBox="0 0 24 24" fill="none" stroke="#2f4db3" stroke-width="2.2" stroke-linecap="round" stroke-linejoin="round">
          <path d="M22 16.9v3a2 2 0 0 1-2.2 2 19.8 19.8 0 0 1-8.6-3.1 19.5 19.5 0 0 1-6-6A19.8 19.8 0 0 1 2.1 4.2 2 2 0 0 1 4.1 2h3a2 2 0 0 1 2 1.7c.1.9.4 1.8.7 2.7a2 2 0 0 1-.5 2.1L8 9.8a16 16 0 0 0 6 6l1.3-1.3a2 2 0 0 1 2.1-.4c.9.3 1.8.6 2.7.7a2 2 0 0 1 1.7 2z"/>
          <path d="M15 5a5 5 0 0 1 4 4"/>
          <path d="M15 1a9 9 0 0 1 8 8"/>
        </svg>
      </span>
      <span class="phone-number">319-555-0187</span>
    </div>

    <div class="brand">
      <div class="brand-name">Harlow Auto</div>
      <div class="brand-town">Marengo, IA</div>
    </div>
  </section>
</div>
</body>
</html>
```